Letterhead to Introduce a 'Sister' Company.

What I am needing is a design for a letter head to introduce our current customers base of (KT Alarm) customers to our new service, 'Kestrel Tide Solar Brokers'

```html
<!DOCTYPE html>
<html lang="en">
<head>
<meta charset="utf-8">
<title>Kestrel Tide Solar Brokers – Letterhead</title>
<link rel="stylesheet" href="https://fonts.googleapis.com/css2?family=Lato:wght@300;400;700&family=Great+Vibes&display=swap">
<style>
  :root{
    --navy:#1e3f70;
    --orange:#f39a1c;
    --ink:#3a3a3a;
    --muted:#555;
    --paper:#ffffff;
    --backdrop:#ececec;
    --placeholder-tone:#ececec;
  }
  *{box-sizing:border-box;margin:0;padding:0}
  html,body{width:1200px;height:1200px;overflow:hidden}
  body{background:var(--backdrop);font-family:'Lato',sans-serif;color:var(--ink)}
  .letterhead{
    position:absolute;left:200px;top:35px;width:800px;height:1130px;
    background:var(--paper);overflow:hidden;
    box-shadow:0 6px 24px rgba(0,0,0,.12);
  }
  .side-curve{position:absolute;left:0;top:0;width:120px;height:1130px}
  .decoration-area{
    position:absolute;left:705px;top:520px;width:95px;height:460px;
    background:linear-gradient(90deg, #f6f6f6, var(--placeholder-tone));
  }
  .brand{position:absolute;left:150px;top:80px;display:flex;align-items:center;gap:12px}
  .brand-dot{width:34px;height:34px;border-radius:50%;background:var(--orange)}
  .brand-name{font-weight:700;font-size:25px;line-height:1.1;color:var(--navy);letter-spacing:.5px}
  .contact{position:absolute;left:560px;top:60px;font-size:11.5px;font-style:normal;line-height:1.55;color:var(--muted)}
  .contact-row{display:flex;align-items:center;gap:7px;padding-left:14px}
  .contact-row svg{width:10px;height:10px;flex:none}
  .recipient{position:absolute;left:190px;top:235px}
  .date{font-size:15px;font-weight:300;color:var(--muted);margin-bottom:10px}
  .recipient-name{font-size:18px;color:var(--orange);text-transform:uppercase}
  .recipient-role{font-size:16px;font-weight:300;margin-bottom:18px}
  .recipient-address{font-size:16px;font-weight:300;line-height:1.3;margin-bottom:22px}
  .salutation{font-size:16px;font-weight:700}
  .body-copy{position:absolute;left:190px;top:470px;width:500px;font-size:12.6px;line-height:1.5;color:var(--ink)}
  .body-copy p{margin-bottom:16px}
  .closing{position:absolute;left:190px;top:880px;font-size:15px;font-weight:300;color:var(--muted)}
  .signature{position:absolute;left:235px;top:900px;font-family:'Great Vibes',cursive;font-size:58px;color:#111}
</style>
</head>
<body>
<main class="letterhead">
  <svg class="side-curve" viewBox="0 0 120 1130" preserveAspectRatio="none" aria-hidden="true">
    <path d="M0 0 C 60 150, 95 420, 86 640 C 78 860, 40 1010, 0 1130 Z" fill="var(--orange)"/>
    <path d="M0 0 C 50 150, 82 420, 74 640 C 66 860, 32 1010, 0 1130 Z" fill="var(--navy)"/>
  </svg>

  <div class="decoration-area" role="img" aria-label="Area for a faint grey sun graphic"></div>

  <header class="brand">
    <span class="brand-dot"></span>
    <span class="brand-name">Kestrel Tide<br>Solar Brokers</span>
  </header>

  <address class="contact">
    <div>2870 Harlow Ridge Road</div>
    <div style="padding-left:7px">Fairmont, GA 31090</div>
    <div class="contact-row"><svg viewBox="0 0 10 10"><circle cx="5" cy="5" r="5" fill="var(--orange)"/><path d="M3 2.5l1 1-.6.8a4 4 0 0 0 2.3 2.3l.8-.6 1 1-.8.9C4.5 7.8 2.2 5.5 2.1 3.3z" fill="#fff"/></svg>555.014.3862</div>
    <div class="contact-row"><svg viewBox="0 0 10 10"><circle cx="5" cy="5" r="5" fill="var(--orange)"/><rect x="2.5" y="4" width="5" height="3" fill="#fff"/></svg>555.014.3862 (Fax)</div>
    <div class="contact-row"><svg viewBox="0 0 10 10"><circle cx="5" cy="5" r="5" fill="var(--orange)"/><path d="M2.5 3.5h5v3h-5z M2.5 3.5l2.5 2 2.5-2" fill="none" stroke="#fff" stroke-width=".8"/></svg>hello@kestreltidesolar.com</div>
    <div class="contact-row"><svg viewBox="0 0 10 10"><circle cx="5" cy="5" r="5" fill="var(--orange)"/><circle cx="5" cy="5" r="2.6" fill="none" stroke="#fff" stroke-width=".8"/><path d="M2.4 5h5.2" stroke="#fff" stroke-width=".7"/></svg>www.kestreltidesolar.com</div>
  </address>

  <section class="recipient">
    <p class="date">September 21-2020</p>
    <p class="recipient-name">Mr. Daniel Reyes</p>
    <p class="recipient-role">President</p>
    <p class="recipient-address">2870 Harlow Ridge Road<br>Fairmont, GA 31090</p>
    <p class="salutation">Dear Mr. Reyes</p>
  </section>

  <section class="body-copy">
    <p>This is Photoshop's version of Lorem Ipsum. Proin gravida nibh vel velit auctor aliquet. Aenean sollicitudin, lorem quis bibendum auctor, nisi elit consequat ipsum, nec sagittis sem nibh id elit. Duis sed odio sit amet nibh vulputate cursus a sit amet mauris. Morbi accumsan ipsum velit. Nam nec tellus a odio tincidunt auctor a ornare odio. Sed non mauris elit.</p>
    <p>This is Photoshop's version of Lorem Ipsum. Proin gravida nibh vel velit auctor aliquet. Aenean sollicitudin, lorem quis bibendum auctor, nisi elit consequat ipsum, nec sagittis sem nibh id elit. Duis sed odio sit amet nibh vulputate cursus a sit amet mauris. Morbi accumsan ipsum velit. Nam nec tellus a odio tincidunt auctor a ornare odio. Sed non mauris elit.</p>
    <p>This is Photoshop's version of Lorem Ipsum. Proin gravida nibh vel velit auctor aliquet. Aenean sollicitudin, lorem quis bibendum auctor, nisi elit consequat ipsum, nec sagittis sem nibh id elit. Duis sed odio sit amet nibh vulputate cursus a sit amet mauris.</p>
    <p>This is Photoshop's version of Lorem Ipsum. Proin gravida nibh vel velit auctor aliquet. Aenean sollicitudin, lorem quis bibendum auctor, nisi elit consequat ipsum.</p>
  </section>

  <p class="closing">Regard</p>
  <p class="signature">Martin Hale</p>
</main>
</body>
</html>
```